Redesign of an insurance website

Attached is an insurance website that I need to redesign. Currently the website is too dark. I like for example www.brenvalo.com . Could you make the website lighter and change the structure a little so that it is more user friendly?

Industry/Entity Type

Insurance

Number of Pages Required

4 page

```html
<!DOCTYPE html>
<html lang="cs">
<head>
<meta charset="utf-8">
<title>Kryjemevas.cz – srovnání pojištění</title>
<link rel="stylesheet" href="https://fonts.googleapis.com/css2?family=PT+Sans:wght@400;700&family=Didact+Gothic&display=swap">
<style>
:root{
  --navy:#1d4477;
  --navy-dark:#183a66;
  --green:#4aa534;
  --green-dark:#3a8a27;
  --green-link:#3f9e35;
  --ink:#1a1a1a;
  --text:#2c2c2c;
  --page:#f4f4f4;
  --footer:#333333;
  --line:#cfcfcf;
}
*{box-sizing:border-box;margin:0;padding:0}
html,body{width:1162px;height:1200px;overflow:hidden}
body{position:relative;background:var(--page);font-family:"Didact Gothic",sans-serif;color:var(--text)}

.site-header{position:absolute;left:0;top:0;width:1162px;height:101px;background:#fff;border-top:2px solid var(--navy)}
.brand{position:absolute;font-family:"PT Sans",sans-serif;font-weight:700;letter-spacing:.3px}
.site-header .brand{left:136px;top:40px;font-size:30px;color:var(--navy)}
.social{position:absolute;left:701px;top:6px;display:flex;gap:4px}
.social span{width:22px;height:22px;border-radius:50%;background:var(--navy)}
.social span:nth-child(2){background:#3f9fd6}
.social span:nth-child(3){background:var(--green)}
.account-tab{position:absolute;left:784px;top:0;width:240px;height:30px}
.account-tab .tab-shape{position:absolute;left:0;top:0}
.account-tab .links{position:absolute;left:20px;top:7px;display:flex;gap:20px;font-family:"PT Sans",sans-serif;font-size:12px;line-height:14px;color:#fff;white-space:nowrap}
.account-tab .links span{display:flex;align-items:center;gap:5px}
.main-nav{position:absolute;top:59px;left:758px;display:flex;font-family:"PT Sans",sans-serif;font-weight:700;font-size:12.5px;color:var(--ink)}
.main-nav a{color:inherit;text-decoration:none;padding:0 22px;border-left:1px solid #ddd;line-height:14px}
.main-nav a:first-child{border-left:0;padding-left:0}
.main-nav a:last-child{padding-right:0}

.hero{position:absolute;left:0;top:101px;width:1162px;height:493px;
  background:linear-gradient(180deg,#1d4a86 0%,#3a78b8 45%,#6da3d4 72%,#4f8a3a 86%,#3f7a2c 100%)}
.hero-copy{position:absolute;left:138px;top:205px;color:#fff}
.hero-copy h1{font-family:"PT Sans",sans-serif;font-weight:700;font-size:25px;margin-bottom:18px}
.benefits{list-style:none;font-size:14px}
.benefits li{display:flex;align-items:center;gap:8px;height:30px}
.tagline{position:absolute;left:0;top:571px;width:670px;height:47px}
.tagline svg{position:absolute;left:0;top:0}
.tagline p{position:absolute;left:139px;top:14px;font-family:"PT Sans",sans-serif;font-weight:700;font-size:16px;color:var(--ink)}

.quote-card{position:absolute;left:702px;top:177px;width:321px;height:485px;background:#fff;border-radius:3px;box-shadow:0 8px 10px -6px rgba(0,0,0,.25)}
.ribbon{position:absolute;left:-34px;top:12px}
.ribbon h2{position:absolute;left:34px;top:28px;width:321px;text-align:center;color:#fff;font-family:"PT Sans",sans-serif;font-weight:700;font-size:22px;line-height:31px}
.field{position:absolute;left:20px;width:283px;height:31px;border:1px solid var(--line);border-radius:3px;font-size:12px;padding:8px 14px;color:#333}
.agree{position:absolute;left:26px;top:276px;display:flex;align-items:center;gap:6px;font-size:13px;color:#222}
.agree .box{width:22px;height:22px;border:1px solid var(--line);position:relative}
.agree svg{position:absolute;left:2px;top:-5px}
.btn{background:var(--green);color:#fff;font-family:"PT Sans",sans-serif;font-weight:700;text-align:center;border-radius:2px}
.quote-card .btn{position:absolute;left:20px;top:310px;width:283px;height:38px;line-height:38px;font-size:13px}
.other{position:absolute;left:20px;top:364px;font-family:"PT Sans",sans-serif;font-weight:700;font-size:12px;color:var(--green-link)}
.types{position:absolute;left:0;top:395px;width:321px;height:90px}
.types .arrow{position:absolute;top:18px}
.type{position:absolute;top:0;width:60px;text-align:center;font-size:10.5px;line-height:10.5px;color:#444}
.type .ico{width:45px;height:45px;border-radius:50%;background:var(--green);margin:0 auto 4px;display:flex;align-items:center;justify-content:center}
.type.active .ico{background:var(--navy)}

.section-title{position:absolute;font-family:"PT Sans",sans-serif;font-weight:700;font-size:17px;color:var(--navy)}
.puzzle-photo{position:absolute;left:137px;top:751px;width:264px;height:219px;border-radius:3px;
  background:radial-gradient(circle at 52% 48%,#c9d8ee 0%,#5b77a6 22%,#253e6b 55%,#0f1f3d 100%)}
.body-copy{position:absolute;font-size:12px;line-height:21px;color:#222;text-align:justify}
.save-btn{position:absolute;left:424px;top:934px;width:133px;height:35px;line-height:35px;font-size:14px}

.newsletter{position:absolute;left:0;top:1022px;width:1162px;height:92px;background:var(--navy)}
.newsletter svg{position:absolute;left:160px;top:29px}
.newsletter h3{position:absolute;left:256px;top:33px;font-family:"PT Sans",sans-serif;font-weight:700;font-size:20px;color:#fff}
.newsletter .email{position:absolute;left:484px;top:26px;width:389px;height:41px;background:#fff;border-radius:2px 0 0 2px;font-style:italic;font-size:11.5px;padding:14px 18px;color:#444}
.newsletter .btn{position:absolute;left:873px;top:26px;width:127px;height:41px;line-height:41px;font-size:15px;letter-spacing:.5px}

.site-footer{position:absolute;left:0;top:1114px;width:1162px;height:86px;background:var(--footer)}
.site-footer .brand{left:139px;top:27px;font-size:28px;color:#fff}
.legal{position:absolute;right:135px;top:24px;text-align:right;font-size:13px;line-height:19px;color:#fff}
</style>
</head>
<body>

<header class="site-header">
  <div class="brand">KRYJEMEVAS.CZ</div>
  <div class="social" aria-label="Sociální sítě"><span></span><span></span><span></span></div>
  <div class="account-tab">
    <svg class="tab-shape" width="240" height="30"><polygon points="0,0 240,0 230,30 10,30" fill="#1d4477"/></svg>
    <div class="links">
      <span><svg width="14" height="12" viewBox="0 0 14 12"><path d="M0 4h6V1l5 5-5 5V8H0z" fill="#fff"/><path d="M9 0h5v12H9v-2h3V2H9z" fill="#fff"/></svg>PRIHLASIT SE</span>
      <span><svg width="14" height="14" viewBox="0 0 14 14"><circle cx="7" cy="4" r="3.5" fill="#fff"/><path d="M1 14c0-4 3-6 6-6s6 2 6 6z" fill="#fff"/></svg>REGISTROVAT</span>
    </div>
  </div>
  <nav class="main-nav"><a href="#">O NAS</a><a href="#">CASTE DOTAZY</a><a href="#">KONTAKT</a></nav>
</header>

<section class="hero" role="img" aria-label="Rodina s dítětem na procházce po zelené louce pod modrou oblohou"></section>

<div class="hero-copy">
  <h1>Proc hledat pojisteni pres kryjemevas.cz?</h1>
  <ul class="benefits">
    <li><svg width="16" height="15" viewBox="0 0 16 15"><rect x="1" y="3" width="11" height="11" fill="none" stroke="#4aa534" stroke-width="1.6"/><path d="M3.5 8l3 3 8-9" fill="none" stroke="#4aa534" stroke-width="2"/></svg>s námi najdete tu nejvýhodnější nabídku</li>
    <li><svg width="16" height="15" viewBox="0 0 16 15"><rect x="1" y="3" width="11" height="11" fill="none" stroke="#4aa534" stroke-width="1.6"/><path d="M3.5 8l3 3 8-9" fill="none" stroke="#4aa534" stroke-width="2"/></svg>zaručíme vám nejlepší cenu na trhu</li>
    <li><svg width="16" height="15" viewBox="0 0 16 15"><rect x="1" y="3" width="11" height="11" fill="none" stroke="#4aa534" stroke-width="1.6"/><path d="M3.5 8l3 3 8-9" fill="none" stroke="#4aa534" stroke-width="2"/></svg>stačí pár minut a můžete ušetřit tisíce</li>
    <li><svg width="16" height="15" viewBox="0 0 16 15"><rect x="1" y="3" width="11" height="11" fill="none" stroke="#4aa534" stroke-width="1.6"/><path d="M3.5 8l3 3 8-9" fill="none" stroke="#4aa534" stroke-width="2"/></svg>srovnáváme všechny pojišťovny</li>
    <li><svg width="16" height="15" viewBox="0 0 16 15"><rect x="1" y="3" width="11" height="11" fill="none" stroke="#4aa534" stroke-width="1.6"/><path d="M3.5 8l3 3 8-9" fill="none" stroke="#4aa534" stroke-width="2"/></svg>zařídíme vám všechny druhy pojištění</li>
    <li><svg width="16" height="15" viewBox="0 0 16 15"><rect x="1" y="3" width="11" height="11" fill="none" stroke="#4aa534" stroke-width="1.6"/><path d="M3.5 8l3 3 8-9" fill="none" stroke="#4aa534" stroke-width="2"/></svg>vše vyřídíte z pohodlí domova</li>
    <li><svg width="16" height="15" viewBox="0 0 16 15"><rect x="1" y="3" width="11" height="11" fill="none" stroke="#4aa534" stroke-width="1.6"/><path d="M3.5 8l3 3 8-9" fill="none" stroke="#4aa534" stroke-width="2"/></svg>nemusíte nikam chodit a ušetříte</li>
  </ul>
</div>

<div class="tagline">
  <svg width="670" height="47"><polygon points="0,0 652,0 670,23.5 652,47 0,47" fill="#4aa534"/><polygon points="0,0 646,0 662,23.5 646,47 0,47" fill="#fff"/></svg>
  <p>OUR INSURANCE PROFESSIONALS ARE ALWAYS THERE FOR YOU</p>
</div>

<div class="quote-card">
  <div class="ribbon">
    <svg width="400" height="130">
      <polygon points="0,120 18,82 40,92" fill="#3a8a27"/>
      <polygon points="355,20 396,38 355,100" fill="#3a8a27"/>
      <polygon points="14,0 355,14 355,103 12,84" fill="#4aa534"/>
    </svg>
    <h2>Najděte nejvýhodnější<br>pojištění</h2>
  </div>
  <div class="field" style="top:143px">Jméno</div>
  <div class="field" style="top:186px">Pnmeni</div>
  <div class="field" style="top:230px">E-mail</div>
  <div class="agree"><div class="box"><svg width="22" height="22" viewBox="0 0 22 22"><path d="M3 12l5 6L20 3" fill="none" stroke="#1d4477" stroke-width="2.6"/></svg></div>Souhlas. s podmínkami pojistit</div>
  <div class="btn">SPOCITAT CENU</div>
  <div class="other">Chcete pojistit neco jineho?</div>
  <div class="types">
    <svg class="arrow" style="left:14px" width="10" height="14"><path d="M8 1L2 7l6 6" fill="none" stroke="#888" stroke-width="2"/></svg>
    <div class="type active" style="left:26px"><div class="ico"><svg width="24" height="20" viewBox="0 0 24 20"><path d="M2 14l4-7h10l5 7v4H2z" fill="#fff"/><circle cx="7" cy="18" r="2" fill="#1d4477"/><circle cx="17" cy="18" r="2" fill="#1d4477"/></svg></div>Havarijní<br>pojištění</div>
    <div class="type" style="left:95px"><div class="ico"><svg width="24" height="24" viewBox="0 0 24 24"><path d="M21 3l-7 7 3 9-2 2-4-7-4 4v3l-2 1-1-4-4-1 1-2h3l4-4-7-4 2-2 9 3 7-7z" fill="#fff"/></svg></div>Cestovní<br>pojištění</div>
    <div class="type" style="left:170px"><div class="ico"><svg width="24" height="22" viewBox="0 0 24 22"><path d="M12 1L1 11h3v10h6v-6h4v6h6V11h3z" fill="#fff"/></svg></div>Pojištění<br>domova</div>
    <div class="type" style="left:236px"><div class="ico"><svg width="26" height="20" viewBox="0 0 26 20"><path d="M4 9l3-7h12l3 7h2v8H2V9z" fill="#fff"/><rect x="8" y="4" width="10" height="5" fill="#4aa534"/><circle cx="7" cy="13" r="2" fill="#4aa534"/><circle cx="19" cy="13" r="2" fill="#4aa534"/></svg></div>Povine<br>ruceni</div>
    <svg class="arrow" style="left:299px" width="10" height="14"><path d="M2 1l6 6-6 6" fill="none" stroke="#888" stroke-width="2"/></svg>
  </div>
</div>

<h2 class="section-title" style="left:136px;top:700px">UZAVŘELI JSTE V MINULOSTI NEVÝHODNOU POJISTKU? ZBAVTE SE JÍ!</h2>
<div class="puzzle-photo" role="img" aria-label="Ruka vkládá svítící dílek skládačky"></div>
<p class="body-copy" style="left:425px;top:748px;width:273px;letter-spacing:.1px">Lorem ipsum dolor sit amet, consectetuer adipiscing elit, sed diam nonummy nibh euismod tincidunt ut laoreet dolore magna aliquam erat volutpat. Ut wisi enim ad minim tationullamcorper suscipit lobortis nisl ut aliquip exeuismod tincidunt ut laoreet dolore magna aliquam erat volutpat. Ut wisi enim ad minim veniam, quis nostrud exerci tation ullamcorperad minim.</p>
<div class="btn save-btn">CHCI UŠETŘIT</div>

<h2 class="section-title" style="left:735px;top:698px">JAK TO FUNGUJE</h2>
<p class="body-copy" style="left:735px;top:748px;width:288px">Lorem ipsum dolor sit amet, consectetuer adipiscing elit, sed diam nonummy nibh euismod tincidunt ut laoreet dolore magna aliquam erat volutpat. Ut wisi enim ad minim tationullamcorper suscipit lobortis nisl ut aliquip exeuismod tincidunt ut laoreet dolore magna aliquam erat volutpat.</p>

<section class="newsletter">
  <svg width="86" height="36" viewBox="0 0 86 36">
    <path d="M0 5h20M3 14h14M0 23h16M4 31h12" stroke="#fff" stroke-width="3"/>
    <polygon points="24,2 84,2 74,34 18,34" fill="none" stroke="#fff" stroke-width="3"/>
    <path d="M24 3l26 17 33-17M20 33l22-15M74 33L62 18" fill="none" stroke="#fff" stroke-width="3"/>
  </svg>
  <h3>ODEBÍRAT NEWSLEUER</h3>
  <div class="email">Enter your email here</div>
  <div class="btn">SUBSCRIBE</div>
</section>

<footer class="site-footer">
  <div class="brand">KRYJEMEVAS.CZ</div>
  <div class="legal">Ochrana soukromi | Podminky pouziti<br>Copyright 2017 Kryjemevas.CZ. Vsechna prava vyhrazena.</div>
</footer>

</body>
</html>
```